Graphic Design Project

We are currently undertaking a new business venture. We have developed a business strategy which we wish to present to our prospective business partner as a one page visual.
The business strategy which we developed is in word format. We would like to be able to present our partner with a chart that is more professional visually.
Ideally we would like to be able to edit the document, so that as the strategy changes we can update it - but this is not essential if it hinders the design. Please let us know what format you will be providing the document in.
I have attached a copy of the chart that we created. When we pick the successful design we will send you our company name and logo be included in the design.
Target Market(s)
We are a training company and our new business venture is with another training and development company
Industry/Entity Type
Business
Requirements
Nice to have
- Editable version

```html
<!DOCTYPE html>
<html lang="en">
<head>
<meta charset="utf-8">
<title>Lumo – Strategy Chart</title>
<link rel="stylesheet" href="https://fonts.googleapis.com/css2?family=PT+Sans:wght@400;700&family=Gelasio:ital,wght@1,400;1,700&display=swap">
<style>
  :root {
    --frame-green: #6cbf0a;
    --canvas-cream: #fffcd1;
    --header-dark: #3f4542;
    --header-mid: #56605b;
    --note-paper: #ffffff;
    --note-fill: #ccf7a9;
    --note-dash: #a6d688;
    --step-top: #8fd25a;
    --step-bottom: #6fa537;
    --arrow-green: #3e7a14;
    --ink: #111111;
    --ink-soft: #2b2b2b;
    --white: #ffffff;
    --pin: #2a2a2a;
  }
  * { box-sizing: border-box; margin: 0; padding: 0; }
  html, body { width: 1200px; height: 1095px; overflow: hidden; }
  body { background: var(--canvas-cream); font-family: "PT Sans", sans-serif; }

  .chart {
    position: relative;
    width: 1200px; height: 1095px;
    background: var(--canvas-cream);
    border: 6px solid var(--frame-green);
  }
  .masthead {
    position: absolute; left: 2px; top: 2px; width: 1184px; height: 112px;
    background: linear-gradient(180deg, var(--header-mid), var(--header-dark));
    border-bottom: 3px solid #e9e6c4;
    display: flex; align-items: center; gap: 14px; padding-left: 92px;
  }
  .brand-dot { width: 46px; height: 46px; border-radius: 50%; background: #7ec83a; }
  .brand-name { font-size: 54px; font-weight: 700; color: var(--white); letter-spacing: 1px; }

  .note {
    position: absolute; width: 171px; height: 172px;
    background: var(--note-paper); padding: 6px;
    border: 1px solid #dcdcdc;
    box-shadow: 0 7px 6px -4px rgba(0,0,0,.35);
  }
  .note.short { height: 115px; }
  .note-body {
    width: 100%; height: 100%;
    background: var(--note-fill);
    border: 1px dashed var(--note-dash);
    padding: 9px 0 0 15px;
  }
  .note::before {
    content: ""; position: absolute; left: 50%; top: -6px;
    width: 5px; height: 5px; margin-left: -6px; border-radius: 50%;
    background: var(--pin);
  }
  .note-title { font-size: 17.5px; color: var(--ink); line-height: 22px; margin-bottom: 5px; }
  .note-line, .step-line {
    font-family: "Gelasio", serif; font-style: italic;
    font-size: 12.5px; line-height: 18.8px; color: var(--ink-soft);
  }

  .step {
    position: absolute; width: 171px; height: 129px;
    background: linear-gradient(180deg, var(--step-top), var(--step-bottom));
    border: 3px solid #f1f4ea; border-radius: 5px;
    box-shadow: 0 2px 6px rgba(0,0,0,.35);
    padding: 10px 0 0 15px;
  }
  .step-title {
    font-size: 20px; font-weight: 700; color: var(--white);
    text-align: center; margin: 0 0 3px -15px; line-height: 26px;
  }
  .step-line { color: var(--white); font-weight: 700; }

  .connectors { position: absolute; left: -6px; top: -6px; pointer-events: none; }
  .connectors use { fill: var(--arrow-green); }
</style>
</head>
<body>
<div class="chart">
  <header class="masthead">
    <span class="brand-dot"></span>
    <span class="brand-name">Lumo</span>
  </header>

  <!-- top notes -->
  <div class="note" style="left:84px;top:163px"><div class="note-body"><p class="note-title">Title Goes Here</p><p class="note-line">Lorem ipsum dolor sit</p><p class="note-line">Lorem ipsum dolor sit</p><p class="note-line">Lorem ipsum dolor sit</p><p class="note-line">Lorem ipsum dolor sit</p><p class="note-line">Lorem ipsum dolor sit</p><p class="note-line">Lorem ipsum dolor sit</p></div></div>
  <div class="note" style="left:303px;top:163px"><div class="note-body"><p class="note-title">Title Goes Here</p><p class="note-line">Lorem ipsum dolor sit</p><p class="note-line">Lorem ipsum dolor sit</p><p class="note-line">Lorem ipsum dolor sit</p><p class="note-line">Lorem ipsum dolor sit</p><p class="note-line">Lorem ipsum dolor sit</p><p class="note-line">Lorem ipsum dolor sit</p></div></div>
  <div class="note" style="left:523px;top:163px"><div class="note-body"><p class="note-title">Title Goes Here</p><p class="note-line">Lorem ipsum dolor sit</p><p class="note-line">Lorem ipsum dolor sit</p><p class="note-line">Lorem ipsum dolor sit</p><p class="note-line">Lorem ipsum dolor sit</p><p class="note-line">Lorem ipsum dolor sit</p><p class="note-line">Lorem ipsum dolor sit</p></div></div>
  <div class="note" style="left:742px;top:163px"><div class="note-body"><p class="note-title">Title Goes Here</p><p class="note-line">Lorem ipsum dolor sit</p><p class="note-line">Lorem ipsum dolor sit</p><p class="note-line">Lorem ipsum dolor sit</p><p class="note-line">Lorem ipsum dolor sit</p><p class="note-line">Lorem ipsum dolor sit</p><p class="note-line">Lorem ipsum dolor sit</p></div></div>
  <div class="note" style="left:962px;top:163px"><div class="note-body"><p class="note-title">Title Goes Here</p><p class="note-line">Lorem ipsum dolor sit</p><p class="note-line">Lorem ipsum dolor sit</p><p class="note-line">Lorem ipsum dolor sit</p><p class="note-line">Lorem ipsum dolor sit</p><p class="note-line">Lorem ipsum dolor sit</p><p class="note-line">Lorem ipsum dolor sit</p></div></div>

  <!-- main steps -->
  <div class="step" style="left:81px;top:396px"><p class="step-title">Title Here</p><p class="step-line">Lorem ipsum dolor sit</p><p class="step-line">Lorem ipsum dolor sit</p><p class="step-line">Lorem ipsum dolor sit</p><p class="step-line">Lorem ipsum dolor sit</p></div>
  <div class="step" style="left:300px;top:396px"><p class="step-title">Title Here</p><p class="step-line">Lorem ipsum dolor sit</p><p class="step-line">Lorem ipsum dolor sit</p><p class="step-line">Lorem ipsum dolor sit</p><p class="step-line">Lorem ipsum dolor sit</p></div>
  <div class="step" style="left:522px;top:396px"><p class="step-title">Title Here</p><p class="step-line">Lorem ipsum dolor sit</p><p class="step-line">Lorem ipsum dolor sit</p><p class="step-line">Lorem ipsum dolor sit</p><p class="step-line">Lorem ipsum dolor sit</p></div>
  <div class="step" style="left:740px;top:396px"><p class="step-title">Title Here</p><p class="step-line">Lorem ipsum dolor sit</p><p class="step-line">Lorem ipsum dolor sit</p><p class="step-line">Lorem ipsum dolor sit</p><p class="step-line">Lorem ipsum dolor sit</p></div>
  <div class="step" style="left:959px;top:396px"><p class="step-title">Title Here</p><p class="step-line">Lorem ipsum dolor sit</p><p class="step-line">Lorem ipsum dolor sit</p><p class="step-line">Lorem ipsum dolor sit</p><p class="step-line">Lorem ipsum dolor sit</p></div>

  <!-- bottom notes -->
  <div class="note" style="left:81px;top:581px"><div class="note-body"><p class="note-title">Title Goes Here</p><p class="note-line">Lorem ipsum dolor sit</p><p class="note-line">Lorem ipsum dolor sit</p><p class="note-line">Lorem ipsum dolor sit</p><p class="note-line">Lorem ipsum dolor sit</p><p class="note-line">Lorem ipsum dolor sit</p><p class="note-line">Lorem ipsum dolor sit</p></div></div>
  <div class="note" style="left:292px;top:581px"><div class="note-body"><p class="note-title">Title Goes Here</p><p class="note-line">Lorem ipsum dolor sit</p><p class="note-line">Lorem ipsum dolor sit</p><p class="note-line">Lorem ipsum dolor sit</p><p class="note-line">Lorem ipsum dolor sit</p><p class="note-line">Lorem ipsum dolor sit</p><p class="note-line">Lorem ipsum dolor sit</p></div></div>
  <div class="note short" style="left:292px;top:788px"><div class="note-body"><p class="note-title">Title Goes Here</p><p class="note-line">Lorem ipsum dolor sit</p><p class="note-line">Lorem ipsum dolor sit</p><p class="note-line">Lorem ipsum dolor sit</p></div></div>
  <div class="note short" style="left:292px;top:933px"><div class="note-body"><p class="note-title">Title Goes Here</p><p class="note-line">Lorem ipsum dolor sit</p><p class="note-line">Lorem ipsum dolor sit</p><p class="note-line">Lorem ipsum dolor sit</p></div></div>
  <div class="note" style="left:520px;top:581px"><div class="note-body"><p class="note-title">Title Goes Here</p><p class="note-line">Lorem ipsum dolor sit</p><p class="note-line">Lorem ipsum dolor sit</p><p class="note-line">Lorem ipsum dolor sit</p><p class="note-line">Lorem ipsum dolor sit</p><p class="note-line">Lorem ipsum dolor sit</p><p class="note-line">Lorem ipsum dolor sit</p></div></div>
  <div class="note" style="left:854px;top:581px"><div class="note-body"><p class="note-title">Title Goes Here</p><p class="note-line">Lorem ipsum dolor sit</p><p class="note-line">Lorem ipsum dolor sit</p><p class="note-line">Lorem ipsum dolor sit</p><p class="note-line">Lorem ipsum dolor sit</p><p class="note-line">Lorem ipsum dolor sit</p><p class="note-line">Lorem ipsum dolor sit</p></div></div>
  <div class="note" style="left:854px;top:791px"><div class="note-body"><p class="note-title">Title Goes Here</p><p class="note-line">Lorem ipsum dolor sit</p><p class="note-line">Lorem ipsum dolor sit</p><p class="note-line">Lorem ipsum dolor sit</p><p class="note-line">Lorem ipsum dolor sit</p><p class="note-line">Lorem ipsum dolor sit</p><p class="note-line">Lorem ipsum dolor sit</p></div></div>

  <svg class="connectors" width="1200" height="1095" viewBox="0 0 1200 1095" aria-hidden="true">
    <defs>
      <path id="arrow" d="M0 0 L14 16 L7 16 L7 36 L-7 36 L-7 16 L-14 16 Z"/>
    </defs>
    <!-- feeds into steps -->
    <use href="#arrow" transform="translate(175.5 392) rotate(180)"/>
    <use href="#arrow" transform="translate(394.5 392) rotate(180)"/>
    <use href="#arrow" transform="translate(614.5 392) rotate(180)"/>
    <use href="#arrow" transform="translate(833.5 392) rotate(180)"/>
    <use href="#arrow" transform="translate(1053.5 392) rotate(180)"/>
    <!-- step to step -->
    <use href="#arrow" transform="translate(303 467) rotate(90)"/>
    <use href="#arrow" transform="translate(522 467) rotate(90)"/>
    <use href="#arrow" transform="translate(744 467) rotate(90)"/>
    <use href="#arrow" transform="translate(962 467) rotate(90)"/>
    <!-- supporting notes -->
    <use href="#arrow" transform="translate(173 539)"/>
    <use href="#arrow" transform="translate(384 539)"/>
    <use href="#arrow" transform="translate(614 539)"/>
    <use href="#arrow" transform="translate(384 760)"/>
    <use href="#arrow" transform="translate(384 905)"/>
    <use href="#arrow" transform="translate(896 540) rotate(-25)"/>
    <use href="#arrow" transform="translate(1018 538) rotate(25)"/>
    <use href="#arrow" transform="translate(946 762)"/>
  </svg>
</div>
</body>
</html>
```